Presentations Guide - Catalogue Design Project

This task is for a booklet for each attendee of our Bright Hearth Living event on March 28, 2013 to use during the event to guide them with a:

-cover page
-schedule for the evening
-contents
-guide to the presentations - including vendor logos (files attached)
-space for notes (just lightly lined pages - preferably similar to
-back cover with contact information

For the text, please just include text blocks in which I can enter the information.

The total number of pages (including front & back covers) should be approximately 16.

Most information can be found at: http://dwellwiseplace.net

Industry/Entity Type

Event

Requirements
Must have
• There is no specific text that you need to upload except for what is written below. If there are text boxes, please just use sample text or lorem ipsum to showcase that.

The final size of the bound booklet can be any of the following:
4" x 9"
5.5" x 8.5"
6" x 6"

Please leave room for a wire and or coil binding on either the left-hand or top side of the booklet.

Page A: Front Cover Page [includes title of event: Bright H. Living Event - Sprint 2013]

Page B: Inside Front Cover Page [schedule of events]

contents:
Page 1: Table of Contents
Page 2: Presentations Guide
Page 3: About Tessellion & Contact Information
Pages 4-20: Note-taking pages

Page C: Inside Back Cover - Sponsors of the event (just provide a space for me to upload the logos of our sponsors)

Page D: Outside Back Cover [includes Tessellion contact information & Tessellion Logo]

```html
<!DOCTYPE html>
<html lang="en">
<head>
<meta charset="utf-8">
<title>Tessellion – Bright H. Living Event – Sprint 2013</title>
<link rel="stylesheet" href="https://fonts.googleapis.com/css2?family=Open+Sans:wght@400&display=swap">
<style>
  :root {
    --amber: #fbb832;
    --leaf: #8dc63f;
    --paper: #ffffff;
    --ink: #1a1a1a;
    --frame: #2b2b2b;
  }
  html, body {
    margin: 0;
    padding: 0;
    width: 776px;
    height: 1200px;
    overflow: hidden;
    background: var(--paper);
  }
  .cover {
    display: block;
    width: 776px;
    height: 1200px;
  }
  .cover__ground { fill: var(--amber); stroke: var(--frame); stroke-width: 1; }
  .cover__page { fill: var(--paper); }
  .cover__swoosh { fill: var(--leaf); }
  .brand__mark { fill: var(--amber); }
  .brand__name {
    font-family: "Open Sans", Arial, sans-serif;
    font-weight: 400;
    font-size: 54px;
    letter-spacing: 2px;
    fill: var(--ink);
  }
  .brand__tagline {
    font-family: "Open Sans", Arial, sans-serif;
    font-weight: 400;
    font-size: 20px;
    fill: var(--ink);
  }
  .season__band { fill: var(--leaf); }
  .season__streak { fill: var(--paper); }
  .event__band { fill: var(--amber); }
  .banner-text {
    font-family: "Open Sans", Arial, sans-serif;
    font-weight: 400;
    fill: var(--ink);
  }
  .season__text { font-size: 25px; }
  .event__text { font-size: 27px; }
</style>
</head>
<body>
<svg class="cover" viewBox="0 0 650 1000" preserveAspectRatio="none" xmlns="http://www.w3.org/2000/svg">
  <rect class="cover__ground" x="0.5" y="0.5" width="649" height="999"/>
  <path class="cover__page" d="M15,90 C150,40 400,18 560,25 C612,40 616,300 620,500 C624,700 624,790 635,815 L635,835 C500,900 350,960 200,940 C90,922 15,800 15,640 Z"/>
  <path class="cover__swoosh" d="M95,872 C165,955 400,950 635,842 L635,897 C430,985 170,980 95,872 Z"/>

  <g class="brand">
    <circle class="brand__mark" cx="138" cy="353" r="16"/>
    <text class="brand__name" x="345" y="372" text-anchor="middle">TESSELLION</text>
    <text class="brand__tagline" x="325" y="455" text-anchor="middle">Made for the way you live.</text>
  </g>

  <g class="season">
    <polygon class="season__band" points="405,608 582,450 600,560 410,645"/>
    <polygon class="season__streak" points="548,485 586,452 560,500"/>
    <polygon class="season__streak" points="562,500 590,475 574,518"/>
    <polygon class="season__streak" points="575,520 594,505 586,535"/>
    <text class="banner-text season__text" transform="translate(425,633) rotate(-41)">Sprint 2013</text>
  </g>

  <g class="event">
    <polygon class="event__band" points="115,812 422,657 434,682 130,845"/>
    <text class="banner-text event__text" transform="translate(178,875) rotate(-35)">Bright H. Living Event</text>
  </g>
</svg>
</body>
</html>
```